hi all

Im after a new age looking business card with my company logo on it

must include these details, I would like the PH and Email to be symbols

If the colours used for card could be kept within the colours used in logo that I have supplied that would be great, if another colour is to be used dark grey would be ok. no light bulbs etc thanks

Details below to be incorporated on card

Damian Holloway

Lic E871302

PH 0219647381

E info@brightvaleelectrical.example.nz

Domestic Commercial Industrial Electricians

```html
<!DOCTYPE html>
<html lang="en">
<head>
<meta charset="utf-8">
<title>Brightvale Electrical – Business Card</title>
<link href="https://fonts.googleapis.com/css2?family=Quicksand:wght@700&display=swap" rel="stylesheet">
<style>
  :root {
    --page: #ffffff;
    --card: #ffffff;
    --card-edge: #1e1e1e;
    --sky: #00adef;
    --sky-deep: #0a8fd0;
    --brand-blue: #1c75bc;
    --charcoal: #282f39;
    --ink: #111111;
    --white: #ffffff;
    --soft-white: #d9dee5;
  }
  * { margin: 0; padding: 0; box-sizing: border-box; }
  html, body {
    width: 1200px;
    height: 1000px;
    overflow: hidden;
    background: var(--page);
  }
  .business-card {
    position: absolute;
    left: 37px;
    top: 162px;
    width: 1127px;
    height: 677px;
    background: var(--card);
    border: 1px solid var(--card-edge);
    overflow: hidden;
  }
  .card-bands {
    position: absolute;
    inset: 0;
    width: 100%;
    height: 100%;
  }
  .contact-icon {
    position: absolute;
    left: 116px;
    width: 56px;
    height: 66px;
  }
  .contact-icon--phone { top: 115px; }
  .contact-icon--email { top: 197px; }
  .contact-text {
    position: absolute;
    font-family: Arial, Helvetica, sans-serif;
    font-size: 24px;
    color: var(--ink);
    white-space: nowrap;
  }
  .contact-text--phone { left: 196px; top: 144px; }
  .contact-text--email { left: 197px; top: 228px; font-size: 23px; }
  .licence { left: 200px; top: 336px; }
  .holder-name {
    position: absolute;
    left: 118px;
    top: 438px;
    font-family: "Quicksand", sans-serif;
    font-weight: 700;
    font-size: 46px;
    color: var(--white);
    white-space: nowrap;
  }
  .company-name {
    position: absolute;
    left: 630px;
    top: 190px;
    display: flex;
    align-items: center;
    gap: 14px;
    font-family: "Quicksand", sans-serif;
    font-weight: 700;
    font-size: 36px;
    color: var(--brand-blue);
    white-space: nowrap;
  }
  .company-name__dot {
    width: 44px;
    height: 44px;
    border-radius: 50%;
    background: var(--brand-blue);
    flex: none;
  }
  .trade-line {
    position: absolute;
    left: 118px;
    top: 604px;
    font-family: Arial, Helvetica, sans-serif;
    font-size: 21px;
    letter-spacing: 1px;
    color: var(--soft-white);
    white-space: nowrap;
  }
</style>
</head>
<body>
  <main class="business-card">
    <svg class="card-bands" viewBox="0 0 1127 677">
      <defs>
        <linearGradient id="skyBand" x1="0" y1="0" x2="1" y2="1">
          <stop offset="0" stop-color="#0a97d8"/>
          <stop offset="0.5" stop-color="#00adef"/>
          <stop offset="1" stop-color="#0b90cf"/>
        </linearGradient>
      </defs>
      <path class="band-sky" role="img" aria-label="Blue band with a faceted geometric network pattern"
            fill="url(#skyBand)"
            d="M0 386 H562 Q578 386 590 376 L616 354 Q630 343 650 343 H1127 V677 H0 Z"/>
      <path class="band-charcoal" fill="#282f39"
            d="M0 563 H562 Q578 563 590 553 L616 530 Q630 518 650 518 H1127 V677 H0 Z"/>
    </svg>

    <svg class="contact-icon contact-icon--phone" viewBox="0 0 56 66" role="img" aria-label="Phone">
      <path d="M6 0 H50 Q56 0 56 6 V66 Q28 50 0 66 V6 Q0 0 6 0 Z" fill="#00adef"/>
      <path d="M28 0 H50 Q56 0 56 6 V66 Q42 56 28 55 Z" fill="#1c75bc" opacity="0.55"/>
      <path d="M16 24 Q28 14 40 24 L38 29 L33 27 L33 24 Q28 22 23 24 L23 27 L18 29 Z" fill="#fff"/>
      <rect x="19" y="30" width="18" height="12" rx="2" fill="#fff"/>
      <g fill="#00adef">
        <rect x="22" y="32" width="3" height="2"/><rect x="27" y="32" width="3" height="2"/><rect x="32" y="32" width="3" height="2"/>
        <rect x="22" y="36" width="3" height="2"/><rect x="27" y="36" width="3" height="2"/><rect x="32" y="36" width="3" height="2"/>
      </g>
    </svg>
    <span class="contact-text contact-text--phone">0219647381</span>

    <svg class="contact-icon contact-icon--email" viewBox="0 0 56 66" role="img" aria-label="Email">
      <path d="M6 0 H50 Q56 0 56 6 V66 Q28 50 0 66 V6 Q0 0 6 0 Z" fill="#00adef"/>
      <path d="M28 0 H50 Q56 0 56 6 V66 Q42 56 28 55 Z" fill="#1c75bc" opacity="0.55"/>
      <g fill="none" stroke="#fff" stroke-width="2">
        <circle cx="28" cy="27" r="12"/>
        <ellipse cx="28" cy="27" rx="5" ry="12"/>
        <path d="M16 27 H40 M18 21 H38 M18 33 H38"/>
      </g>
      <path d="M33 32 L33 42 L36 39 L39 44 L41 43 L38 38 L42 38 Z" fill="#fff"/>
    </svg>
    <span class="contact-text contact-text--email">info@brightvaleelectrical.example.nz</span>

    <span class="contact-text licence">Lic E871302</span>

    <div class="company-name">
      <span class="company-name__dot"></span>
      <span>Brightvale Electrical</span>
    </div>

    <h1 class="holder-name">Damian Holloway</h1>

    <p class="trade-line">Domestic · Commercial · Industrial Electricians</p>
  </main>
</body>
</html>
```